Invite to The Halvorsen Project

You’re Cordially Invited
To a Sunset Celebration Honoring the Launch of The Halvorsen

Date: Thursday, May 15
Time: 5:30 PM – 7:30 PM
Location: The Halvorsen, 214 Quillfield Street, East Boston

Please join us for an elegant evening of connection and celebration as we unveil The Halvorsen Project.
Enjoy private tours of Units 3 and 4, along with our breathtaking roof deck offering sweeping views of East Boston at sunset.

Sip curated selections of beer and wine and savor light seasonal bites as you mingle with colleagues and guests.

Feel free to bring clients, friends, or family — all are welcome!

Kindly RSVP to:
Marisol Penwarden, Larchmont Realty
📧 Marisol@larchmontexample.com

Please include logo, classic design, and attachments. Colors navy, gold, white

```html
<!DOCTYPE html>
<html lang="en">
<head>
<meta charset="utf-8">
<title>Sunset Celebration – The Halvorsen Invitation</title>
<link rel="stylesheet" href="https://fonts.googleapis.com/css2?family=Cinzel:wght@400;500;600&family=Montserrat:wght@300;400;700&display=swap">
<style>
  :root {
    --navy: #1f2a4d;
    --gold: #d3a94f;
    --gold-deep: #b8862e;
    --gold-light: #f0d48a;
    --white: #ffffff;
    --ink-soft: #3c4566;
    --backdrop: #5e5859;
    --sketch: #eeeef0;
  }
  * { margin: 0; padding: 0; box-sizing: border-box; }
  html, body { width: 1200px; height: 2215px; overflow: hidden; }
  body { background: var(--backdrop); position: relative; font-family: "Montserrat", sans-serif; color: var(--navy); }

  .invitation {
    position: absolute; left: 62px; top: 345px;
    width: 1076px; height: 1524px;
    background: var(--white);
    overflow: hidden;
  }
  .invitation > * { position: absolute; }

  .building-sketch {
    left: 0; top: 470px; width: 1076px; height: 1054px;
    background: linear-gradient(180deg, rgba(238,238,240,0) 0%, var(--sketch) 25%, var(--sketch) 80%, #e8e8ea 100%);
    opacity: .8;
  }
  .frame { left: 0; top: 0; width: 1076px; height: 1524px; }

  .banner-text {
    left: 104px; top: 39px; width: 870px; height: 60px;
    display: flex; align-items: center; justify-content: center;
    font-family: "Montserrat", sans-serif; font-weight: 400;
    font-size: 30px; letter-spacing: 9px; color: var(--white);
  }

  .headline { left: 0; top: 130px; width: 1076px; height: 240px; }
  .headline .lead { font-family: "Cinzel", serif; font-size: 34px; fill: var(--navy); }
  .headline .title { font-family: "Cinzel", serif; font-weight: 400; fill: url(#goldFoil); }

  .honoring {
    left: 0; top: 382px; width: 1076px; text-align: center;
    font-family: "Cinzel", serif; font-weight: 500;
    font-size: 41px; line-height: 49px; letter-spacing: 3px; color: var(--navy);
  }

  .rule { height: 2px; background: var(--gold); }
  .rule--short { left: 474px; width: 128px; }
  .rule--top { top: 533px; }
  .rule--mid { top: 849px; }
  .rule--long { left: 111px; width: 855px; top: 1239px; height: 1.5px; }

  .event-date {
    left: 0; top: 578px; width: 1076px; text-align: center;
    font-size: 53px; font-weight: 400; letter-spacing: -0.5px;
  }
  .event-time { left: 0; top: 649px; width: 1076px; text-align: center; font-size: 25px; }
  .venue-name { left: 0; top: 696px; width: 1076px; text-align: center; font-size: 26px; font-weight: 700; }
  .venue-address { left: 0; top: 732px; width: 1076px; text-align: center; font-size: 25px; }

  .details {
    left: 148px; top: 890px; width: 780px; text-align: center;
    font-size: 22.5px; line-height: 30.5px; font-weight: 400;
  }
  .details p + p { margin-top: 27px; }

  .welcome {
    left: 0; top: 1126px; width: 1076px; text-align: center;
    font-family: "Cinzel", serif; color: var(--ink-soft);
  }
  .welcome .note { font-size: 23px; line-height: 34px; letter-spacing: 1px; }
  .welcome .all { font-size: 30px; line-height: 40px; letter-spacing: 1.5px; }

  .rsvp { left: 112px; top: 1280px; width: 520px; font-size: 23px; line-height: 31px; }
  .rsvp .label, .rsvp .company { font-weight: 300; }
  .rsvp .contact { font-weight: 700; font-size: 24px; }
  .rsvp .email { margin-top: 22px; display: flex; align-items: center; gap: 24px; font-weight: 300; }
  .rsvp .email svg { flex: none; }

  .brand { left: 693px; top: 1285px; width: 300px; text-align: center; }
  .brand .mark {
    width: 92px; height: 92px; margin: 0 auto 8px;
    border: 3px solid var(--gold); border-radius: 50%;
  }
  .brand .name {
    font-family: "Cinzel", serif; font-weight: 500;
    font-size: 27px; line-height: 30px; letter-spacing: 2px; color: var(--gold);
  }
</style>
</head>
<body>
  <main class="invitation">
    <div class="building-sketch" role="img" aria-label="Faint pencil illustration of the Halvorsen townhouse building with a parked car on the street"></div>

    <svg class="frame" viewBox="0 0 1076 1524" aria-hidden="true">
      <path d="M99,39 H977 A60 60 0 0 0 1037,99 V1425 A60 60 0 0 0 977,1485 H99 A60 60 0 0 0 39,1425 V99 A60 60 0 0 0 99,39 Z"
            fill="none" stroke="#d3a94f" stroke-width="2"/>
      <path d="M104,39 H974 C946,39 940,99 912,99 H168 C140,99 132,39 104,39 Z" fill="#d3a94f"/>
    </svg>
    <div class="banner-text">YOU’RE CORDIALLY INVITED</div>

    <svg class="headline" viewBox="0 130 1076 240">
      <defs>
        <linearGradient id="goldFoil" x1="0" y1="0" x2="1" y2="1">
          <stop offset="0" stop-color="#b8862e"/>
          <stop offset=".35" stop-color="#f0d48a"/>
          <stop offset=".6" stop-color="#c99a3e"/>
          <stop offset="1" stop-color="#e2bd68"/>
        </linearGradient>
      </defs>
      <text class="lead" x="216" y="178">TO A</text>
      <text class="title" x="315" y="248" font-size="132" textLength="450" lengthAdjust="spacingAndGlyphs">SUNSET</text>
      <text class="title" x="118" y="353" font-size="136" textLength="833" lengthAdjust="spacingAndGlyphs">CELEBRATION</text>
    </svg>

    <h1 class="honoring">HONORING THE LAUNCH OF<br>THE HALVORSEN</h1>

    <div class="rule rule--short rule--top"></div>
    <p class="event-date">THURSDAY, MAY 15</p>
    <p class="event-time">5:30 PM – 7:30 PM</p>
    <p class="venue-name">THE HALVORSEN</p>
    <p class="venue-address">214 Quillfield Street, East Boston</p>
    <div class="rule rule--short rule--mid"></div>

    <div class="details">
      <p>Please join us for an elegant evening of connection and celebration as we unveil The Halvorsen Project. Enjoy private tours of Units 3 and 4, along with our breathtaking roof deck offering sweeping views of East Boston at sunset.</p>
      <p>Sip curated selections of beer and wine and savor light seasonal bites as you mingle with colleagues and guests.</p>
    </div>

    <div class="welcome">
      <p class="note">FEEL FREE TO BRING CLIENTS, FRIENDS, OR FAMILY -</p>
      <p class="all">ALL ARE WELCOME!</p>
    </div>

    <div class="rule rule--long"></div>

    <div class="rsvp">
      <p class="label">Kindly RSVP to:</p>
      <p class="contact">MARISOL PENWARDEN</p>
      <p class="company">Larchmont Realty</p>
      <p class="email">
        <svg width="24" height="18" viewBox="0 0 24 18" aria-hidden="true">
          <rect x="0" y="0" width="24" height="18" fill="#d3a94f"/>
          <path d="M1,1 L12,10 L23,1" fill="none" stroke="#ffffff" stroke-width="1.8"/>
        </svg>
        Marisol@larchmontexample.com
      </p>
    </div>

    <div class="brand">
      <div class="mark"></div>
      <p class="name">LARCHMONT<br>REALTY</p>
    </div>
  </main>
</body>
</html>
```